Mavro Scrub - Contact/Landing Page

I need a landing page which will essentially be the page that customers will go to from the 'website' link on GMB listing. It will provide a short overview of services which need to be selectable. a little further down can capture some contact details followed by a large Submit Now button etc...

I have some icon/logo's that can be utilised at the bottom of the page as industry type references.

Target Market(s)

End of Lease Cleaning Services

Industry/Entity Type

Cleaning Service

Colors

Designer to choose colors to be used in the design.

Requirements
Must have
• As per description
Should not have
• Colours to match my website mavroscrub.com.au

```html
<!DOCTYPE html>
<html lang="en">
<head>
<meta charset="utf-8">
<title>Mavro Scrub – Contact</title>
<link href="https://fonts.googleapis.com/css2?family=Crimson+Pro:wght@400;700&family=Karla:wght@400&family=Roboto:wght@400;500&display=swap" rel="stylesheet">
<style>
:root{
  --brand:#3a78bc;
  --brand-light:#5ab4e4;
  --ink:#2b2b2b;
  --soft:#f1f7fc;
  --line:#cfd6dd;
  --white:#ffffff;
}
*{box-sizing:border-box;margin:0;padding:0}
html,body{width:837px;height:1200px;overflow:hidden;background:var(--white)}
body{position:relative;font-family:"Karla",sans-serif;color:var(--ink)}
.hero{position:absolute;left:0;top:0;width:837px;height:414px;background:var(--brand)}
.hero-brand{position:absolute;left:0;right:0;top:140px;text-align:center;font-family:"Crimson Pro",serif;font-weight:700;font-size:64px;color:var(--white);line-height:1}
.hero-mark{position:absolute;left:398px;top:80px;width:40px;height:40px;border-radius:50%;background:var(--brand-light)}
.tagline{position:absolute;left:0;right:0;top:336px;text-align:center;font-family:"Crimson Pro",serif;font-size:26px;color:var(--white)}
.tagline .divider{margin:0 14px}
.service{position:absolute;top:456px;width:221px;height:161px;background:var(--white);box-shadow:0 0 6px rgba(0,0,0,.08);text-align:center}
.service h2{font-family:"Crimson Pro",serif;font-weight:400;font-size:27px;margin-top:21px;line-height:1.1}
.service p{font-size:12.5px;line-height:19.5px;margin:8px 18px 0;color:#333}
.select{position:absolute;left:0;right:0;top:124px;font-family:"Roboto",sans-serif;font-size:12px;font-weight:500;color:var(--brand);display:flex;justify-content:center;align-items:center;gap:6px}
.select svg{width:11px;height:11px}
.contact{position:absolute;left:0;top:667px;width:837px;height:309px;background:var(--soft);overflow:hidden}
.contact-watermark{position:absolute;left:600px;top:150px;font-family:"Crimson Pro",serif;font-weight:700;font-size:64px;color:#e3eef8;line-height:1}
.contact h1{position:absolute;left:135px;top:42px;font-family:"Crimson Pro",serif;font-weight:700;font-size:27px;color:#333;letter-spacing:.3px}
.field{position:absolute;left:135px;width:314px;height:31px;display:flex;align-items:center}
.field label{width:70px;font-size:11.5px}
.field .input{width:244px;height:31px;background:var(--white);border:1px solid var(--line)}
.send{position:absolute;left:475px;top:81px;width:237px;height:82px;background:var(--white);border:1px solid var(--line)}
.send .email{text-align:center;font-family:"Roboto",sans-serif;font-size:14.5px;margin-top:9px}
.send .submit{position:absolute;left:6px;top:37px;width:225px;height:38px;background:linear-gradient(100deg,var(--brand) 30%,var(--brand-light));color:var(--white);font-family:"Roboto",sans-serif;font-weight:500;font-size:13px;display:flex;align-items:center;justify-content:center}
.badge{position:absolute;top:1030px;height:44px;border-radius:4px}
.footer{position:absolute;left:0;top:1144px;width:837px;height:56px;background:linear-gradient(90deg,var(--brand-light),var(--brand) 80%);color:var(--white);font-size:11.5px}
.footer .copy{position:absolute;left:70px;top:20px}
.footer .social{position:absolute;left:404px;top:14px;width:29px;height:29px;border:1px solid var(--white);border-radius:50%}
.footer .licence{position:absolute;right:70px;top:18px;font-family:"Roboto",sans-serif;font-size:13px}
</style>
</head>
<body>
<header class="hero">
  <div class="hero-mark"></div>
  <div class="hero-brand">Mavro Scrub</div>
  <p class="tagline">End of Lease Cleaning<span class="divider">|</span>Licensed Pest Control</p>
</header>

<section class="services">
  <article class="service" style="left:85px">
    <h2>Cleaning</h2>
    <p>All interior cleaning carried out to property management requirements</p>
    <div class="select">SELECT <svg viewBox="0 0 11 11"><rect x=".75" y=".75" width="9.5" height="9.5" fill="none" stroke="#3a78bc" stroke-width="1.2"/></svg></div>
  </article>
  <article class="service" style="left:316px">
    <h2>Carpet Cleaning</h2>
    <p>Carpet stacam cleaning to Australian Standard As 3733:1995</p>
    <div class="select">SELECT <svg viewBox="0 0 11 11"><path d="M10 5.5v4.7H.75V.75H7" fill="none" stroke="#3a78bc" stroke-width="1.2"/><path d="M3 5l2.2 2.3L10.5 1.3" fill="none" stroke="#3a78bc" stroke-width="1.3"/></svg></div>
  </article>
  <article class="service" style="left:547px">
    <h2>Pest Control</h2>
    <p>Mandatory requirement for pets on premises</p>
    <div class="select">SELECT <svg viewBox="0 0 11 11"><rect x=".75" y=".75" width="9.5" height="9.5" fill="none" stroke="#3a78bc" stroke-width="1.2"/></svg></div>
  </article>
</section>

<section class="contact">
  <div class="contact-watermark">Mavro<br>Scrub</div>
  <h1>HOW CAN WE HELP YOU?</h1>
  <div class="field" style="top:80px"><label>First Name*</label><div class="input"></div></div>
  <div class="field" style="top:118px"><label>sur Name*</label><div class="input"></div></div>
  <div class="field" style="top:156px"><label>Email*</label><div class="input"></div></div>
  <div class="field" style="top:195px"><label>Phone*</label><div class="input"></div></div>
  <div class="field" style="top:233px"><label>Suburb*</label><div class="input"></div></div>
  <div class="send">
    <p class="email">info@mavroscrub.com.au</p>
    <div class="submit">SUBMIT</div>
  </div>
</section>

<section class="partners">
  <div class="badge" role="img" aria-label="Certification badge" style="left:66px;width:106px;background:#1a1a1a"></div>
  <div class="badge" role="img" aria-label="Partner badge" style="left:225px;width:128px;background:#c8cde0"></div>
  <div class="badge" role="img" aria-label="Training partner badge" style="left:417px;width:72px;background:#2d4a8c"></div>
  <div class="badge" role="img" aria-label="Environmental studies badge" style="left:530px;width:133px;height:40px;top:1032px;border-radius:0;background:#8cbf3f"></div>
  <div class="badge" role="img" aria-label="Environment authority badge" style="left:696px;width:71px;background:#1d4f91"></div>
</section>

<footer class="footer">
  <span class="copy">© 2021 Mavro Scrub. All Rights Reserved</span>
  <span class="social" aria-label="Social link"></span>
  <span class="licence">PEST LICENCE: 5184026</span>
</footer>
</body>
</html>
```